Notepads for Marketing pieces-BOLD design

Looking for notepads for marketing pieces with logo, phone number, and website. Maybe something faded in background. Looking for bold and different

```html
<!DOCTYPE html>
<html lang="en">
<head>
<meta charset="utf-8">
<title>VitalCrest Notepad 76mm x 76mm</title>
<link rel="stylesheet" href="https://fonts.googleapis.com/css2?family=Montserrat:wght@600&family=Barlow:wght@600;800&family=Barlow+Semi+Condensed:wght@600;700&display=swap">
<style>
  :root {
    --backdrop: #b3b3b3;
    --paper: #ffffff;
    --brand-red: #f20000;
    --ink: #000000;
    --faint-red: #fdeeee;
    --faint-edge: #eeeeee;
  }
  html, body {
    margin: 0;
    padding: 0;
    width: 1200px;
    height: 962px;
    overflow: hidden;
    background: var(--backdrop);
  }
  .stage {
    position: relative;
    width: 1200px;
    height: 962px;
  }
  .format-label {
    position: absolute;
    right: 252px;
    top: 70px;
    margin: 0;
    text-align: right;
    color: var(--paper);
    font-family: "Montserrat", sans-serif;
    font-weight: 600;
    font-size: 39px;
    line-height: 46px;
    letter-spacing: 2px;
  }
  .notepad {
    position: absolute;
    left: 249px;
    top: 189px;
    width: 703px;
    height: 703px;
    background: var(--paper);
    overflow: hidden;
  }
  .notepad-graphics {
    position: absolute;
    inset: 0;
  }
  .brand-head {
    position: absolute;
    right: 25px;
    top: 52px;
    text-align: center;
  }
  .brand-name {
    margin: 0;
    font-family: "Barlow", sans-serif;
    font-weight: 800;
    font-size: 42px;
    line-height: 44px;
    letter-spacing: 1px;
    color: var(--brand-red);
  }
  .services {
    margin: 10px 0 0;
    font-family: "Barlow", sans-serif;
    font-weight: 600;
    font-size: 13px;
    color: var(--ink);
    white-space: nowrap;
  }
  .services .divider {
    color: var(--brand-red);
    margin: 0 3px;
  }
  .footer-band {
    position: absolute;
    left: 0;
    right: 0;
    bottom: 0;
    height: 85px;
    font-family: "Barlow Semi Condensed", sans-serif;
    color: var(--paper);
  }
  .contact {
    position: absolute;
    display: flex;
    align-items: center;
  }
  .contact-icon {
    width: 32px;
    height: 32px;
    flex: none;
  }
  .contact-phone { left: 44px; top: 14px; }
  .contact-web { left: 257px; top: 19px; }
  .contact-lines { margin-left: 15px; }
  .phone-number {
    display: block;
    font-weight: 700;
    font-size: 20px;
    line-height: 24px;
    letter-spacing: 0.6px;
  }
  .fax-number {
    display: block;
    font-weight: 700;
    font-size: 16.5px;
    line-height: 22px;
    letter-spacing: 0.5px;
  }
  .fax-number .fax-label { color: var(--brand-red); }
  .web-address {
    margin-left: 10px;
    font-weight: 600;
    font-size: 19px;
    letter-spacing: 0.4px;
  }
  .footer-brand {
    position: absolute;
    right: 30px;
    top: 26px;
    margin: 0;
    font-family: "Barlow", sans-serif;
    font-weight: 800;
    font-size: 27px;
    letter-spacing: 0.5px;
    color: var(--paper);
  }
</style>
</head>
<body>
<main class="stage">
  <p class="format-label">STICKY NOTE<br>76mm x 76mm</p>

  <section class="notepad" aria-label="VitalCrest notepad sheet">
    <svg class="notepad-graphics" width="703" height="703" viewBox="0 0 703 703" aria-hidden="true">
      <polygon points="0,0 103,0 0,131" fill="var(--brand-red)"/>
      <polygon points="112,0 148,0 0,187 0,143" fill="var(--ink)"/>
      <circle cx="555" cy="385" r="96" fill="var(--faint-red)" stroke="var(--faint-edge)" stroke-width="8"/>
      <rect x="0" y="618" width="703" height="85" fill="var(--ink)"/>
      <path d="M0,608 H455 L467,578 L480,626 L491,600 L498,608 H703"
            fill="none" stroke="var(--paper)" stroke-width="16" stroke-linejoin="miter"/>
      <path d="M0,608 H455 L467,578 L480,626 L491,600 L498,608 H703"
            fill="none" stroke="var(--brand-red)" stroke-width="6" stroke-linejoin="miter"/>
      <polygon points="470,618 490,618 480,646" fill="var(--paper)"/>
    </svg>

    <header class="brand-head">
      <h1 class="brand-name">VITALCREST</h1>
      <p class="services">Home Health<span class="divider">|</span>Medical Staffing<span class="divider">|</span>Outpatient Therapy</p>
    </header>

    <footer class="footer-band">
      <div class="contact contact-phone">
        <svg class="contact-icon" viewBox="0 0 32 32" aria-hidden="true">
          <circle cx="16" cy="16" r="16" fill="var(--brand-red)"/>
          <path d="M11.5,8.5 l3,0.5 1,4 -2,1.5 a11,11 0 0 0 4.5,4.5 l1.5,-2 4,1 0.5,3 -2,2 a13,13 0 0 1 -12.5,-12.5 z" fill="var(--paper)"/>
        </svg>
        <div class="contact-lines">
          <span class="phone-number">1-800-555-0142</span>
          <span class="fax-number"><span class="fax-label">Fax:</span> 866-555-0178</span>
        </div>
      </div>
      <div class="contact contact-web">
        <svg class="contact-icon" viewBox="0 0 32 32" aria-hidden="true">
          <circle cx="16" cy="16" r="16" fill="var(--brand-red)"/>
          <g fill="none" stroke="var(--paper)" stroke-width="1.6">
            <circle cx="16" cy="16" r="9"/>
            <ellipse cx="16" cy="16" rx="4" ry="9"/>
            <line x1="7" y1="16" x2="25" y2="16"/>
            <line x1="8.5" y1="11.5" x2="23.5" y2="11.5"/>
            <line x1="8.5" y1="20.5" x2="23.5" y2="20.5"/>
          </g>
        </svg>
        <span class="web-address">www.vitalcrest.org</span>
      </div>
      <p class="footer-brand">VITALCREST</p>
    </footer>
  </section>
</main>
</body>
</html>
```